Asia based real estate financing firm needs and AWESOME design for a biz card -Harbor Lending Circle

Looking for a stylish, & corporate-looking business card for a real estate financing brokerage firm in Asia, offering global mortgage loans. I uploaded our current logos. We would like to add a splash of color (perhaps the house icon) or any other suggestions are open. For the winning designer, we have a lot of work! Thanks and best of luck!

Target Market(s)

Real estate investors globally. We want to look more like a BANK and NOT a real estate company. Please don't play up on a "house" design.

Industry/Entity Type

Banking

Contact Information for Business Card

Harbor Lending Circle
Peter Wilks
Co-Founder | Partner

14 Cassia Lane, Suite 310
Singapore 047219
www.hlc-example.asia
peterwilks@hlc-example.asia
+65 555-0142
WeChat: peterwilks

Colors

Designer to choose colors to be used in the design.

Requirements
Must have
• Must have the standard business requirements for a card; name, address, email, etc
• Can be horizontal or vertical.
Nice to have
• It would be great to see some sort of variation to the logo with a pop of color. Red is good as we're in Asia, however, other options work as well.
• Our tag line is - Borderless mortgages. It doesn't have to be on the card but might be nice.
• I'd like to start seeing our tagline within the cards as well. - Borderless mortgages.
• Also, please add our location. The location for this card is Singapore so perhaps it can be highlighted or emphasised in some way.
• Singapore | Hong Kong | Shanghai | Manila
• As we will soon open an office in Shanghai, having an option for both languages would be great.
Should not have
• I'm exceited and open to your creativity ... knock it out of the park!

```html
<!DOCTYPE html>
<html lang="en">
<head>
<meta charset="utf-8">
<title>Harbor Lending Circle – Business Card</title>
<link href="https://fonts.googleapis.com/css2?family=Montserrat:wght@400;500;600&display=swap" rel="stylesheet">
<style>
  :root {
    --backdrop: #1f1f1f;
    --brand-red: #bf2025;
    --brand-red-deep: #9a171b;
    --paper: #ececee;
    --ink-grey: #6b6b6b;
    --rule-grey: #b9b9bb;
    --white: #ffffff;
  }
  * { margin: 0; padding: 0; box-sizing: border-box; }
  html, body {
    width: 1200px; height: 1200px; overflow: hidden;
    background: var(--backdrop);
    font-family: "Montserrat", sans-serif;
  }
  .card {
    position: absolute;
    left: 184px;
    width: 832px;
    height: 472px;
  }
  .card--front { top: 90px; background: var(--brand-red); }
  .card--back  { top: 640px; background: var(--paper); }

  .front__brand {
    position: absolute; left: 0; right: 0; top: 178px;
    text-align: center;
    color: var(--brand-red-deep);
    font-weight: 600;
    font-size: 40px;
    letter-spacing: 3px;
    text-transform: uppercase;
  }
  .front__tagline {
    position: absolute; left: 0; right: 0; top: 400px;
    text-align: center;
    color: var(--white);
    font-size: 24px; font-weight: 400;
  }

  .back__brand {
    position: absolute; left: 60px; width: 320px; top: 185px;
    text-align: center;
    color: var(--brand-red);
    font-weight: 600;
    font-size: 30px;
    line-height: 1.25;
    letter-spacing: 2px;
    text-transform: uppercase;
  }
  .back__divider {
    position: absolute; left: 420px; top: 108px;
    width: 1px; height: 246px;
    background: var(--rule-grey);
  }
  .back__details {
    position: absolute; left: 448px; top: 100px;
    color: var(--ink-grey);
  }
  .person__name {
    color: var(--brand-red);
    font-size: 36px; font-weight: 500; line-height: 1.2;
  }
  .person__title { font-size: 18px; margin-top: 2px; }
  .office-address { font-size: 18.5px; line-height: 26px; margin-top: 16px; }
  .contact-list { list-style: none; margin-top: 18px; font-size: 18.5px; }
  .contact-list li { display: flex; align-items: center; height: 26px; }
  .contact-list svg { width: 14px; height: 14px; margin-right: 10px; flex: none; }
  .back__cities {
    position: absolute; left: 0; right: 0; top: 390px;
    text-align: center;
    color: var(--ink-grey);
    font-size: 24px;
  }
</style>
</head>
<body>
  <section class="card card--front">
    <div class="front__brand">Harbor Lending Circle</div>
    <p class="front__tagline">Borderless mortgages</p>
  </section>

  <section class="card card--back">
    <div class="back__brand">Harbor<br>Lending Circle</div>
    <div class="back__divider"></div>
    <div class="back__details">
      <h1 class="person__name">Peter Wilks</h1>
      <p class="person__title">Co-Founder | Partner</p>
      <p class="office-address">14 Cassia Lane, Suite 310<br>Singapore 047219</p>
      <ul class="contact-list">
        <li>
          <svg viewBox="0 0 14 14" aria-hidden="true"><path fill="#bf2025" d="M3 1l2 .5 1 3-1.5 1.2c.8 1.6 2 2.8 3.6 3.6L9.3 7.8l3 1 .5 2-1.6 1.9C6 12.5 1.5 8 1.3 2.6z"/></svg>
          +65 555-0142
        </li>
        <li>
          <svg viewBox="0 0 14 14" aria-hidden="true"><circle cx="7" cy="7" r="6" fill="#bf2025"/></svg>
          peterwilks
        </li>
        <li>
          <svg viewBox="0 0 14 14" aria-hidden="true"><rect x="1" y="3" width="12" height="9" fill="#bf2025"/><path d="M1.5 3.5L7 8l5.5-4.5" stroke="#ececee" stroke-width="1.2" fill="none"/></svg>
          peterwilks@hlc-example.asia
        </li>
        <li>
          <svg viewBox="0 0 14 14" aria-hidden="true"><g fill="none" stroke="#bf2025" stroke-width="1.2"><circle cx="7" cy="7" r="5.8"/><ellipse cx="7" cy="7" rx="2.5" ry="5.8"/><path d="M1.2 7h11.6M2 4h10M2 10h10"/></g></svg>
          www.hlc-example.asia
        </li>
      </ul>
    </div>
    <p class="back__cities">Singapore | Hong Kong | Shanghai | Manila</p>
  </section>
</body>
</html>
```